House Builder and Property Development Card Design and Logo

I need a business card design for a building and property development company.
Colour scheme of Dark Grey and Green, I would like it bold, sharp and professional.
No logo yet done, I'm open to options but please stay away from the usual- house, roof, hammers etc.
Thanks Rob

Please be aware that on the business card information section the WHRC # 5528391 is a licence number and my phone number 0492837165. The numbers are close together and could be mistaken as one whole number 

Thank you

                                   

Industry/Entity Type

Building

Contact Information for Business Card

VARGA BUILD & DEVELOPMENT.
Residential Building & Property Development
Robert Varga - Director
WHRC # 5528391
0492837165
rob@vargabuild.example.com.au

Requirements
Must have
• Bold Business name
Dark grey and green colours
Should not have
• roof outline or hammer logo

```html
<!DOCTYPE html>
<html lang="en">
<head>
<meta charset="utf-8">
<title>Varga Build &amp; Development – Business Card</title>
<link rel="stylesheet" href="https://fonts.googleapis.com/css2?family=Open+Sans:wght@400;600&display=swap">
<style>
  :root {
    --charcoal: #1f2427;
    --lime: #b4ee0f;
    --white: #ffffff;
    --stage: #d9d9d6;
    --paper: #ffffff;
    --ink: #23282b;
  }
  * { box-sizing: border-box; margin: 0; padding: 0; }
  html, body { width: 1200px; height: 1000px; overflow: hidden; }
  body {
    font-family: "Open Sans", Arial, sans-serif;
    background: var(--stage);
    position: relative;
  }
  .stage { position: absolute; left: 0; top: 0; width: 1200px; height: 805px; }
  .card {
    position: absolute;
    width: 525px; height: 300px;
    background: var(--charcoal);
    overflow: hidden;
    box-shadow: 0 6px 18px rgba(0,0,0,.25);
  }
  /* Front */
  .card-front { left: 45px; top: 250px; }
  .card-front .edge-bar {
    position: absolute; left: 0; top: 0; width: 10px; height: 100%;
    background: var(--lime);
  }
  .wordmark { display: flex; align-items: center; gap: 14px; color: var(--lime); font-weight: 400; }
  .wordmark .mark-square { width: 34px; height: 34px; background: var(--lime); flex: none; }
  .wordmark .name { font-size: 42px; line-height: 1; letter-spacing: .5px; }
  .wordmark .sub { font-size: 13px; line-height: 1.3; letter-spacing: .3px; display: block; }
  .card-front .wordmark {
    position: absolute; left: 50%; top: 50%; transform: translate(-50%, -50%);
  }
  /* Back */
  .card-back { left: 630px; top: 250px; }
  .card-back .wordmark-small {
    position: absolute; left: 24px; top: 22px;
    width: 30px; height: 30px; background: var(--lime);
  }
  .tagline-row {
    position: absolute; left: 0; top: 72px; width: 100%;
    display: flex; align-items: center; gap: 10px;
  }
  .tagline-row .bar { height: 9px; background: var(--lime); }
  .tagline-row .bar-left { width: 40px; }
  .tagline-row .bar-right { flex: 1; margin-right: 0; }
  .tagline { color: var(--white); font-size: 15px; white-space: nowrap; }
  .person { position: absolute; left: 26px; top: 118px; }
  .person .full-name { color: var(--lime); font-size: 17px; }
  .person .role { color: var(--white); font-size: 16px; margin-top: 2px; }
  .card-back .wordmark {
    position: absolute; right: 26px; top: 112px;
    display: block; text-align: right;
  }
  .card-back .wordmark .name { font-size: 27px; }
  .card-back .wordmark .sub { font-size: 10px; }
  .contact {
    position: absolute; right: 26px; top: 178px;
    text-align: right; font-size: 14px; line-height: 1.55; color: var(--white);
  }
  .contact .licence { color: var(--lime); }
  .contact .line { display: flex; justify-content: flex-end; align-items: center; gap: 7px; }
  .contact svg { width: 13px; height: 13px; }
  .card-back .base-stripe {
    position: absolute; left: 0; bottom: 0; width: 100%; height: 12px;
    background: var(--lime); border-top: 3px solid var(--white);
  }
  /* Logo presentation band */
  .logo-band {
    position: absolute; left: 0; top: 805px; width: 1200px; height: 195px;
    background: var(--paper);
  }
  .logo-stacked {
    position: absolute; left: 45px; top: 40px;
    display: flex; flex-direction: column; align-items: flex-start; gap: 10px;
    color: var(--ink);
  }
  .logo-stacked .mark-square { width: 70px; height: 70px; background: var(--lime); }
  .logo-stacked .name { font-size: 24px; line-height: 1; }
  .logo-stacked .sub { font-size: 11px; }
  .logo-horizontal {
    position: absolute; left: 765px; top: 50px;
    display: flex; align-items: center; gap: 26px; color: var(--ink);
  }
  .logo-horizontal .mark-square { width: 90px; height: 90px; background: var(--lime); }
  .logo-horizontal .name { font-size: 50px; line-height: 1; }
  .logo-horizontal .sub { font-size: 19px; margin-top: 4px; }
</style>
</head>
<body>
  <section class="stage">
    <article class="card card-front">
      <div class="edge-bar"></div>
      <div class="wordmark">
        <div class="mark-square"></div>
        <div>
          <span class="name">VARGA</span>
          <span class="sub">BUILD &amp; DEVELOPMENT</span>
        </div>
      </div>
    </article>

    <article class="card card-back">
      <div class="wordmark-small"></div>
      <div class="tagline-row">
        <span class="bar bar-left"></span>
        <span class="tagline">Residential Building &amp; Property Development</span>
        <span class="bar bar-right"></span>
      </div>
      <div class="person">
        <div class="full-name">Robert Varga</div>
        <div class="role">Director</div>
      </div>
      <div class="wordmark">
        <span class="name">VARGA</span>
        <span class="sub">BUILD &amp; DEVELOPMENT</span>
      </div>
      <div class="contact">
        <div class="licence">WHRC # 5528391</div>
        <div class="line">
          <svg viewBox="0 0 13 13" aria-hidden="true"><rect x="3" y="0.5" width="7" height="12" rx="1.2" fill="none" stroke="#b4ee0f" stroke-width="1.2"/></svg>
          <span>0492837165</span>
        </div>
        <div class="line">
          <svg viewBox="0 0 13 13" aria-hidden="true"><rect x="0.6" y="2.5" width="11.8" height="8" fill="none" stroke="#ffffff" stroke-width="1.1"/><path d="M0.6 2.5 L6.5 7 L12.4 2.5" fill="none" stroke="#ffffff" stroke-width="1.1"/></svg>
          <span>rob@vargabuild.example.com.au</span>
        </div>
      </div>
      <div class="base-stripe"></div>
    </article>
  </section>

  <section class="logo-band">
    <div class="logo-stacked">
      <div class="mark-square"></div>
      <div>
        <span class="name">VARGA</span>
        <span class="sub">BUILD &amp; DEVELOPMENT</span>
      </div>
    </div>
    <div class="logo-horizontal wordmark">
      <div class="mark-square"></div>
      <div>
        <span class="name">VARGA</span>
        <span class="sub">BUILD &amp; DEVELOPMENT</span>
      </div>
    </div>
  </section>
</body>
</html>
```